Top Scottish IT Company - Web Banner

We want a banner for our main web page that graphically conveys the following values for our IT support company (in the priority order listed)....

a. Secure (your network will be)
b. Pro-Active (management of IT)
c. Expert (in IT systems)
d. Reliable (your network will be)
e. Innovative (our approach is)

Note - I do not want the list of text above to be simply listed in the design - I want them to be inferred by the design - so far as is possible.

The strap line "Expert in maintaing reliable and secure IT networks" - or very similar.

Size of image = 967*240 pixels.

Company Name - Dunmore Systems Ltd - named after the explorer Tobias Dunmore (Current Website = www.dunsysnet.co.uk)

The brief has been updated in light of the first few responses that relied too heavily on the text - it is a banner image we preffer not simply a rpetition of the text in the breif.

Hope this helps.
Neville

Target Market(s)

UK based SME's with large investment in and dependency on IT.

Industry/Entity Type

It Company

Requirements
Must have
• Must Portray IT Secuirty and ProActive apporach to IT management.

```html
<!DOCTYPE html>
<html lang="en">
<head>
<meta charset="utf-8">
<title>Dunmore Systems Ltd – IT Support Banner</title>
<link href="https://fonts.googleapis.com/css2?family=Arimo:wght@400;700&display=swap" rel="stylesheet">
<style>
  :root {
    --frame: #0b1f4a;
    --sky-deep: #0a3d8f;
    --sky-mid: #1f6fd1;
    --sky-pale: #d8ecfb;
    --gold-top: #fff6a8;
    --gold-bottom: #f0b400;
    --title-edge: #2a2200;
    --white: #ffffff;
    --tick: #bfe6ff;
    --band-text: #1b2b45;
    --band-light: #ffffff;
    --band-shade: #c9d3dd;
  }
  * { margin: 0; padding: 0; box-sizing: border-box; }
  html, body {
    width: 1200px;
    height: 298px;
    overflow: hidden;
    background: var(--white);
  }
  .banner {
    position: relative;
    width: 1200px;
    height: 298px;
    overflow: hidden;
    border: 3px solid var(--frame);
    background:
      radial-gradient(ellipse 420px 200px at 560px 120px, var(--sky-pale) 0%, rgba(216,236,251,0) 70%),
      linear-gradient(180deg, var(--sky-mid) 0%, var(--sky-deep) 100%);
    font-family: "Arimo", Arial, sans-serif;
  }
  .data-stream {
    position: absolute;
    left: 715px; top: 20px;
    width: 380px; height: 230px;
    border-radius: 50%;
    background: radial-gradient(circle at 55% 50%, #cfe7fb 0%, #4f95dc 45%, rgba(15,70,150,0) 75%);
    opacity: .85;
  }
  .sweep {
    position: absolute;
    left: 0; top: 0;
    width: 1200px; height: 298px;
  }
  .security-laptop {
    position: absolute;
    left: 0; top: 22px;
    width: 320px; height: 226px;
    border-radius: 8px;
    background: linear-gradient(150deg, #5a7aa8 0%, #1a2c4d 55%, #c9a548 100%);
  }
  .team-photo {
    position: absolute;
    left: 900px; top: 8px;
    width: 297px; height: 290px;
    background: linear-gradient(180deg, #e4c8b4 0%, #3a3d46 45%, #15161b 100%);
  }
  .title {
    position: absolute;
    z-index: 2;
    left: 280px; top: 42px;
    width: 480px;
    text-align: center;
    white-space: nowrap;
    font-size: 31px;
    font-weight: 700;
    line-height: 36px;
    color: var(--gold-bottom);
    background: linear-gradient(180deg, var(--gold-top) 15%, var(--gold-bottom) 80%);
    -webkit-background-clip: text;
    background-clip: text;
    -webkit-text-fill-color: transparent;
    -webkit-text-stroke: 1.2px var(--title-edge);
    filter: drop-shadow(2px 2px 1px rgba(0,0,0,.5));
  }
  .values { list-style: none; }
  .value {
    position: absolute;
    z-index: 2;
    display: flex;
    align-items: center;
    gap: 9px;
    font-size: 24px;
    font-weight: 700;
    line-height: 28px;
    color: var(--white);
    text-shadow: 1px 1px 2px rgba(0,0,0,.55);
    white-space: nowrap;
  }
  .value svg { width: 25px; height: 25px; flex: none; }
  .value--secure     { left: 334px; top: 92px; }
  .value--expert     { left: 551px; top: 92px; }
  .value--proactive  { left: 334px; top: 123px; }
  .value--reliable   { left: 551px; top: 123px; }
  .value--innovative { left: 427px; top: 161px; }
  .web-address {
    position: absolute;
    z-index: 2;
    left: 748px; top: 219px;
    font-size: 16px;
    color: var(--white);
    text-shadow: 1px 1px 2px rgba(0,0,0,.7);
  }
  .strapline {
    position: absolute;
    z-index: 2;
    left: 230px; top: 257px;
    font-size: 21px;
    line-height: 24px;
    font-weight: 400;
    letter-spacing: .3px;
    color: var(--band-text);
    text-transform: uppercase;
    white-space: nowrap;
  }
</style>
</head>
<body>
  <div class="banner">
    <div class="data-stream" role="img" aria-label="Flowing tunnel of binary digits"></div>

    <svg class="sweep" viewBox="0 0 1200 298" aria-hidden="true">
      <defs>
        <linearGradient id="bandFill" x1="0" y1="0" x2="0" y2="1">
          <stop offset="0" stop-color="#ffffff"/>
          <stop offset="1" stop-color="#c9d3dd"/>
        </linearGradient>
        <linearGradient id="arcFill" x1="0" y1="0" x2="1" y2="0">
          <stop offset="0" stop-color="#ffffff" stop-opacity=".9"/>
          <stop offset="1" stop-color="#ffffff" stop-opacity="0"/>
        </linearGradient>
      </defs>
      <path d="M250 235 C 450 190, 650 150, 900 95 L 900 105 C 650 165, 450 205, 250 245 Z" fill="url(#arcFill)"/>
      <path d="M40 298 L40 262 Q40 248 58 248 L1200 248 L1200 298 Z" fill="url(#bandFill)"/>
    </svg>

    <div class="security-laptop" role="img" aria-label="Laptop on its side with a golden security padlock clasped through it"></div>
    <div class="team-photo" role="img" aria-label="Two smiling IT consultants in business suits"></div>

    <h1 class="title">OUR IT SUPPORT COMPANY</h1>

    <ul class="values">
      <li class="value value--secure"><svg viewBox="0 0 24 24"><path d="M3 13 L9 19 L21 4" fill="none" stroke="var(--tick)" stroke-width="4" stroke-linecap="round" stroke-linejoin="round"/></svg>Secure</li>
      <li class="value value--expert"><svg viewBox="0 0 24 24"><path d="M3 13 L9 19 L21 4" fill="none" stroke="var(--tick)" stroke-width="4" stroke-linecap="round" stroke-linejoin="round"/></svg>Expert</li>
      <li class="value value--proactive"><svg viewBox="0 0 24 24"><path d="M3 13 L9 19 L21 4" fill="none" stroke="var(--tick)" stroke-width="4" stroke-linecap="round" stroke-linejoin="round"/></svg>Pro - Active</li>
      <li class="value value--reliable"><svg viewBox="0 0 24 24"><path d="M3 13 L9 19 L21 4" fill="none" stroke="var(--tick)" stroke-width="4" stroke-linecap="round" stroke-linejoin="round"/></svg>Reliable</li>
      <li class="value value--innovative"><svg viewBox="0 0 24 24"><path d="M3 13 L9 19 L21 4" fill="none" stroke="var(--tick)" stroke-width="4" stroke-linecap="round" stroke-linejoin="round"/></svg>Innovative</li>
    </ul>

    <p class="web-address">Dunsysnet.co.uk</p>
    <p class="strapline">Expert in maintaning reliable and secure IT networks</p>
  </div>
</body>
</html>
```